Need a business card for our overland brand!

We had the logo made and we need a great design for our business card. Use the logo provide or tweak it however you see fit.

Contact Information for Business Card

Name, Title, Telephone, email, website

```html
<!DOCTYPE html>
<html lang="en">
<head>
<meta charset="utf-8">
<title>Ridgeline Expeditions – Business Card</title>
<link href="https://fonts.googleapis.com/css2?family=Montserrat:wght@400;600;800&display=swap" rel="stylesheet">
<style>
  :root {
    --navy: #253851;
    --teal: #1fa0c2;
    --white: #ffffff;
    --stage: #ababab;
    --ink-grey: #6b6b6b;
    --rule-grey: #a9a9a9;
  }
  * { margin: 0; padding: 0; box-sizing: border-box; }
  html, body {
    width: 1200px;
    height: 1000px;
    overflow: hidden;
    background: var(--stage);
    font-family: "Montserrat", sans-serif;
  }
  .canvas { position: relative; width: 1200px; height: 1000px; }

  .card {
    position: absolute;
    width: 613px;
    height: 352px;
    border-radius: 22px;
    overflow: hidden;
    background: var(--white);
  }

  /* Front side */
  .card-front { left: 293px; top: 161px; background: var(--navy); }
  .front-brand {
    position: absolute;
    top: 44px; left: 0; right: 0;
    text-align: center;
    color: var(--white);
    font-weight: 800;
    font-size: 30px;
    line-height: 36px;
    letter-spacing: 1px;
  }
  .mountain-art {
    position: absolute;
    left: 0; right: 0; bottom: 0;
    height: 240px;
    background: linear-gradient(to bottom,
      var(--navy) 0%,
      var(--teal) 30%,
      var(--teal) 45%,
      #bfe6f0 62%,
      var(--white) 74%,
      var(--white) 100%);
  }

  /* Back side */
  .card-back { left: 294px; top: 556px; }
  .brand-name {
    position: absolute;
    top: 64px; left: 0; right: 0;
    text-align: center;
    color: var(--navy);
    font-weight: 800;
    font-size: 29px;
    line-height: 38px;
    letter-spacing: 0.5px;
  }
  .contact-row {
    position: absolute;
    top: 192px; left: 0; right: 0;
    height: 38px;
  }
  .person {
    position: absolute;
    right: 322px; top: 1px;
    text-align: right;
  }
  .person-name {
    color: var(--teal);
    font-weight: 600;
    font-size: 16.5px;
    letter-spacing: 0.6px;
    line-height: 20px;
  }
  .person-title {
    color: var(--navy);
    font-size: 11px;
    letter-spacing: 3px;
    margin-right: -3px;
    line-height: 16px;
  }
  .divider {
    position: absolute;
    left: 306px; top: 0;
    width: 2px; height: 37px;
    background: var(--rule-grey);
  }
  .contact-list {
    position: absolute;
    left: 324px; top: 1px;
    list-style: none;
    color: var(--ink-grey);
    font-size: 14.5px;
    line-height: 18px;
  }
  .contact-list li { display: flex; align-items: center; gap: 7px; }
  .contact-list svg { width: 13px; height: 13px; fill: var(--teal); flex: none; }

  .footer-rule {
    position: absolute;
    left: 0; right: 0; top: 297px;
    height: 4px;
    background: var(--teal);
  }
  .footer-band {
    position: absolute;
    left: 0; right: 0; top: 305px; bottom: 0;
    background: var(--navy);
    color: var(--white);
    font-size: 17px;
    text-align: center;
    line-height: 47px;
    letter-spacing: 0.3px;
  }
</style>
</head>
<body>
<div class="canvas">
  <section class="card card-front">
    <div class="mountain-art" role="img" aria-label="Snow-capped mountain range illustration in teal and white"></div>
    <div class="front-brand">RIDGELINE<br>EXPEDITIONS</div>
  </section>

  <section class="card card-back">
    <div class="brand-name">RIDGELINE<br>EXPEDITIONS</div>

    <div class="contact-row">
      <div class="person">
        <div class="person-name">NAME SURNAME</div>
        <div class="person-title">TITLE</div>
      </div>
      <div class="divider"></div>
      <ul class="contact-list">
        <li>
          <svg viewBox="0 0 24 24" aria-hidden="true"><path d="M6.6 10.8a15.1 15.1 0 0 0 6.6 6.6l2.2-2.2c.3-.3.7-.4 1-.2 1.1.4 2.3.6 3.6.6.6 0 1 .4 1 1V20c0 .6-.4 1-1 1A17 17 0 0 1 3 4c0-.6.4-1 1-1h3.5c.6 0 1 .4 1 1 0 1.3.2 2.5.6 3.6.1.3 0 .7-.2 1z"/></svg>
          1234-567-890
        </li>
        <li>
          <svg viewBox="0 0 24 24" aria-hidden="true"><path d="M2 5h20v14H2z"/><path d="M2 5l10 8 10-8" fill="none" stroke="#fff" stroke-width="2"/></svg>
          email@website.com
        </li>
      </ul>
    </div>

    <div class="footer-rule"></div>
    <div class="footer-band">www.website.com</div>
  </section>
</div>
</body>
</html>
```